Thank you card

I want to design the thank you card which encloses in the very package when we ship out. The card has to look nice and useful that people don't want to through away.
I'll submit the words content later.
Here is the content of thank you note and refund policy, I want to make it fun, make clients smile: Dear

When we received your order, the centaur who prints them rushed to my office with overwhelming joy to inform me that it was you who wanted to buy RWD Skincare products. He then galloped down the hall with clanking hooves to deliver your precious order to production. All the water that went into your oder was carefully checked by the mermaids for purity and the forest nymphs made certain only the highest quality ingredients went into your order. Your products were then carefully transported by magic carpet to shipping while being escorted by two genies. The products you ordered were then lovely placed into the package before being transported to the sacred grove to be blessed by Mother Nature herself.

Your package was then transported to the delivery service in a armored car with a unicorn trotting in front of it. It was then left in their care with strict instructions that this was to be delivered to a very important person. RWD Skincare truly appreciates your business and we thank you from the bottom of our hearts for choosing our all natural, environmental safe products.

In the unlikely case you are dissatisfied in any way with our products, feel free to contact us for a full refund. You can keep the products ordered. You simply have to tell us in detail what keep you from feeling fully happy. We wish you health, wealth and happiness.

Warmly

Lien Thu Vo

Target Market(s)

People who are fun, creative, love science also fairy tale, organic.

Font styles to use
Script

Requirements
Must have
• The logo - just the round logo the word change RWD SKINCARE larger, Radiant Willow Dew under.
• some feature of fairy tales, elves, ect, flowers,
• Folding card Thank you with rwd logo
• Inside: wording will be provided Here is the content of thank you note and refund policy, I want to make it fun, make clients smile: Dear
• When we received your order, the centaur who prints them rushed to my office with overwhelming joy to inform me that it was you who wanted to buy RWD Skincare products. He then galloped down the hall with clanking hooves to deliver your precious order to production. All the water that went into your oder was carefully checked by the mermaids for purity and the forest nymphs made certain only the highest quality ingredients went into your order. Your products were then carefully transported by magic carpet to shipping while being escorted by two genies. The products you ordered were then lovely placed into the package before being transported to the sacred grove to be blessed by Mother Nature herself.
• Your package was then transported to the delivery service in an armored car with a unicorn trotting in front of it. It was then left in their care with strict instructions that this was to be delivered to a very important person. RWD Skincare truly appreciates your business and we thank you from the bottom of our hearts for choosing our all-natural, environmentally safe products.
• In the unlikely case, you are dissatisfied in any way with our products, feel free to contact us for a full refund. You can keep the products ordered. You simply have to tell us in detail what keeps you from feeling fully happy. We wish you health, wealth and happiness.
• Warmly
• Lien Thu Vo
• when card open can stick on refrigerator the 1st page and 4page enclose some use full info about herbs ( content will be provided)
Nice to have
• The card can be used as bookmark, or poster with useful info, so beautiful that people don't want to give away.
• The theme of fairy tales.

```html
<!DOCTYPE html>
<html lang="en">
<head>
<meta charset="utf-8">
<title>RWD Skincare – Thank You Card</title>
<link rel="stylesheet" href="https://fonts.googleapis.com/css2?family=Dancing+Script:wght@400;600&family=Open+Sans:wght@400;600;700&family=Playball&display=swap">
<style>
  :root{
    --backdrop:#d6d6d6;
    --paper:#ffffff;
    --lime-top:#a6d817;
    --lime-mid:#c4e515;
    --lime-fade:#eef7b8;
    --ink-green:#2e5a1c;
    --link-green:#7e9c10;
    --brand-green:#3f6f12;
    --brand-gold:#d8b400;
    --navy:#1e2388;
    --ribbon:#f3f78c;
    --letter-ink:#222222;
  }
  *{box-sizing:border-box;margin:0;padding:0}
  html,body{width:1200px;height:1005px;overflow:hidden;background:var(--backdrop)}
  .canvas{position:relative;width:1200px;height:1005px}

  .spread{position:absolute;left:260px;width:680px;height:476px;display:flex;box-shadow:0 6px 14px rgba(0,0,0,.18)}
  .spread--outside{top:14px}
  .spread--inside{top:515px}
  .page{position:relative;width:340px;height:476px;overflow:hidden;background:var(--paper)}

  /* outside spread */
  .spread--outside .page{background:linear-gradient(180deg,var(--lime-top) 0%,var(--lime-mid) 40%,var(--lime-fade) 72%,var(--paper) 86%)}
  .back__panel{position:absolute;left:41px;top:58px;width:253px;height:349px;background:var(--paper);border-radius:22px 22px 0 0}
  .garland{position:absolute;left:38px;width:260px;height:46px;border-radius:23px;
    background:linear-gradient(90deg,#3d8a2a,#e04aa0 20%,#4aa13a 40%,#e04aa0 60%,#3d8a2a 80%,#e04aa0)}
  .garland--top{top:32px}
  .garland--bottom{top:383px}
  .back__notes{position:absolute;left:52px;top:100px;width:232px;font-family:"Open Sans",sans-serif;font-size:8.3px;line-height:11px;color:var(--ink-green);text-align:center}
  .back__notes p{margin-bottom:11px}
  .back__url{position:absolute;left:0;width:340px;top:447px;text-align:center;font-family:"Open Sans",sans-serif;font-weight:700;font-size:8.6px;color:var(--link-green)}

  .front__scene{position:absolute;left:38px;top:46px;width:262px;height:290px;border-radius:48% 48% 20px 20px;
    background:radial-gradient(circle at 52% 30%,#b9a6e8 0%,#e7a9d6 30%,#9fd6ee 60%,rgba(196,229,21,0) 78%)}
  .front__banner{position:absolute;left:28px;top:318px;width:284px;height:62px}
  .front__logo{position:absolute;left:0;top:388px;width:340px;text-align:center}
  .logo__dot{display:block;margin:0 auto 4px;width:42px;height:42px;border-radius:50%;background:var(--brand-gold)}
  .logo__name{font-family:"Dancing Script",cursive;font-weight:600;font-size:19px;line-height:20px;color:var(--brand-green)}
  .logo__tag{font-family:"Open Sans",sans-serif;font-size:5.8px;letter-spacing:.3px;color:var(--brand-green);margin-top:2px}

  /* inside spread */
  .spread--inside .page:first-child{border-right:1px solid #ececec}
  .letter__gift{position:absolute;left:49px;top:30px;width:119px;height:101px;border-radius:10px;
    background:linear-gradient(180deg,#a685d6 0%,#e76fa5 50%,#7cc34a 100%)}
  .letter{font-family:"Dancing Script",cursive;font-size:10.6px;line-height:13.4px;color:var(--letter-ink);text-align:justify}
  .letter--left{position:absolute;left:48px;top:150px;width:256px}
  .letter--right{position:absolute;left:41px;top:78px;width:258px}
  .letter__greeting{margin-bottom:12px}
  .letter p{margin-bottom:12px}
  .letter__closing{margin-top:6px;text-align:left}
  .letter__trees{position:absolute;left:226px;top:320px;width:100px;height:140px;border-radius:40px 40px 6px 6px;
    background:linear-gradient(180deg,#8cc63f 0%,#5e9e2c 60%,#a5683a 100%)}
</style>
</head>
<body>
<main class="canvas">

  <section class="spread spread--outside">
    <article class="page back">
      <div class="back__panel"></div>
      <div class="garland garland--top" role="img" aria-label="Garland of green leaves and pink flowers"></div>
      <div class="back__notes">
        <p>Lorem ipsum dolor sit amet, consectetur adipiscing elit, sed do eiusmod tempor incididunt ut labore et dolore magna aliqua. Ut enim ad minim veniam.</p>
        <p>Lorem ipsum dolor sit amet, consectetur adipiscing elit, sed do eiusmod tempor incididunt ut labore et dolore magna aliqua. Ut enim ad minim veniam.</p>
        <p>Lorem ipsum dolor sit amet, consectetur adipiscing elit, sed do eiusmod tempor incididunt ut labore et dolore magna aliqua. Ut enim ad minim veniam.</p>
        <p>Lorem ipsum dolor sit amet, consectetur adipiscing elit, sed do eiusmod tempor incididunt ut labore et dolore magna aliqua. Ut enim ad minim veniam.</p>
        <p>Lorem ipsum dolor sit amet, consectetur adipiscing elit, sed do eiusmod tempor incididunt ut labore et dolore magna aliqua. Ut enim ad minim veniam.</p>
        <p>Lorem ipsum dolor sit amet, consectetur adipiscing elit, sed do eiusmod tempor incididunt ut labore et dolore magna aliqua. Ut enim ad minim veniam.</p>
      </div>
      <div class="garland garland--bottom" role="img" aria-label="Garland of green leaves and pink flowers"></div>
      <div class="back__url">www.rwdskincare.com</div>
    </article>

    <article class="page front">
      <div class="front__scene" role="img" aria-label="Fairy-tale illustration: a girl with pastel hair riding a unicorn and hugging a gift box, on a rainbow above clouds, with stars and leafy sprigs"></div>
      <svg class="front__banner" viewBox="0 0 284 62" aria-hidden="false">
        <path d="M4 20 L36 18 L30 34 L40 52 L6 50 L18 35 Z" fill="var(--ribbon)" stroke="var(--navy)" stroke-width="2.5" stroke-linejoin="round"/>
        <path d="M280 20 L248 18 L254 34 L244 52 L278 50 L266 35 Z" fill="var(--ribbon)" stroke="var(--navy)" stroke-width="2.5" stroke-linejoin="round"/>
        <path d="M30 10 Q142 -2 254 10 L254 46 Q142 34 30 46 Z" fill="var(--ribbon)" stroke="var(--navy)" stroke-width="2.5" stroke-linejoin="round"/>
        <text x="142" y="36" text-anchor="middle" font-family="Playball, cursive" font-size="31" fill="var(--navy)">Thank You!</text>
      </svg>
      <div class="front__logo">
        <span class="logo__dot"></span>
        <div class="logo__name">RWD Skincare</div>
        <div class="logo__tag">RADIANT WILLOW DEW</div>
      </div>
    </article>
  </section>

  <section class="spread spread--inside">
    <article class="page">
      <div class="letter__gift" role="img" aria-label="Striped gift box with a bow among green bushes and little stars"></div>
      <div class="letter letter--left">
        <div class="letter__greeting">Dear</div>
        <p>When we received your order, the centaur who prints them rushed to my office with overwhelming joy to inform me that it was you who wanted to buy RWD Skincare products. He then galloped down the hall with clanking hooves to deliver your precious order to production. All the water that went into your oder was carefully checked by the mermaids for purity and the forest nymphs made certain only the highest quality ingredients went into your order. Your products were then carefully transported by magic carpet to shipping while being escorted by two genies. The products you ordered were then lovely placed into the package before being transported to the sacred grove to be blessed by Mother Nature herself.</p>
      </div>
    </article>
    <article class="page">
      <div class="letter letter--right">
        <p>Your package was then transported to the delivery service in an armored car with a unicorn trotting in front of it. It was then left in their care with strict instructions that this was to be delivered to a very important person. RWD Skincare truly appreciates your business and we thank you from the bottom of our hearts for choosing our all-natural, environmentally safe products.</p>
        <p>In the unlikely case, you are dissatisfied in any way with our products, feel free to contact us for a full refund. You can keep the products ordered. You simply have to tell us in detail what keeps you from feeling fully happy. We wish you health, wealth and happiness.</p>
        <div class="letter__closing">Warmly<br>Lien Thu Vo</div>
      </div>
      <div class="letter__trees" role="img" aria-label="Two leafy fairy-tale trees with flowers and small scattered stars"></div>
    </article>
  </section>

</main>
</body>
</html>
```